依頼詳細
【外貨両替】
外貨両替は学校へ出向いて行う、出張両替とご自宅へ外貨をお届けする外貨宅配の2プランがございます。どちらのプランにするかは学校の意向や参加者の規模や要望によります。

【フェリシオンクレスト】
外貨両替(現金)以外のお金としてトラベルマネーカード(フェリシオンクレスト)の紹介をしております。こちらはキャッシュレスに対応したカードで使い方はクレジットカードと同じですが、チャージした金額の範囲でご利用頂けるカードです。

今回、制作するパンフレットは旅行会社から旅行参加者へ配布してご質問等があれば旅行会社ではなく直接当社が窓口となり、旅行参加者からの質問等を受付いたします。
今回制作するパンフレットとは別に両替の申込書面、フェリシオンクレストの申込書面は別となります。あくまでも全体の案内、問い合わせ先の案内をするパンフレットです。
記載項目
資料を添付致しますので、要点をまとめてA4サイズカラー裏表で制作をお願い致します。
サイズ
A4
ページ数
両面
希望イメージ
シンプル 複雑
単色 カラフル
暗い 明るい
日常 高級
遊び心 厳粛
未来的 伝統的
女性的 男性的
希望する色
赤系、青系
納品ファイル
• イラストレーター形式 (.ai)
補足説明
■ 選んだ理由

社内で選考した結果、一番わかりやすく好評であった為当選とさせていただきました。

■ 提案者全員のお礼・コメント

この度は短期間でしたが、沢山の方にご参加頂き、またどの提案も良いものばかりでした。
また次回依頼する場合も宜しくお願い致します。

```html
<!DOCTYPE html>
<html lang="ja">
<head>
<meta charset="utf-8">
<title>教育旅行 外貨準備サービスのご案内</title>
<link href="https://fonts.googleapis.com/css2?family=Noto+Sans+JP:wght@400;500;700;900&family=Montserrat:wght@700&display=swap" rel="stylesheet">
<style>
:root{
  --red:#d7192b;
  --navy:#14245a;
  --blue:#1d3f8f;
  --text:#222;
  --white:#fff;
  --photo-a:#e9e2d6;
  --photo-b:#b9a88e;
}
*{margin:0;padding:0;box-sizing:border-box}
html,body{width:851px;height:1200px;overflow:hidden;background:#fff}
body{font-family:"Noto Sans JP",sans-serif;color:var(--text)}
ul{list-style:none}
.flyer{position:relative;width:851px;height:1200px;overflow:hidden;background:var(--white)}
.backdrop{position:absolute;left:0;top:40px;width:851px;height:1053px;
  background:linear-gradient(160deg,#f4f1ec 0%,var(--photo-a) 45%,var(--photo-b) 100%)}
.top-band{position:absolute;left:0;top:0;width:851px;height:40px;background:var(--red);
  color:var(--white);font-weight:700;font-size:19px;text-align:center;line-height:40px;letter-spacing:1px}
.headline{position:absolute;left:30px;top:50px;width:800px;font-weight:900;font-size:56px;
  line-height:66px;color:var(--navy);text-shadow:0 0 6px #fff,0 0 6px #fff}
.headline em{font-style:normal;color:var(--red)}
.tags{position:absolute;left:30px;top:256px;display:flex;gap:10px}
.tag{background:var(--red);color:var(--white);font-weight:700;font-size:18px;padding:1px 14px;line-height:28px}
.intro{position:absolute;left:30px;top:298px;width:600px;font-size:13.5px;line-height:23px;
  font-weight:500;background:rgba(255,255,255,.8);padding:6px 8px}
.audience{position:absolute;left:30px;top:470px;font-weight:700;font-size:17px;line-height:26px;color:var(--navy);
  background:rgba(255,255,255,.85);padding:0 8px}
.audience::before{content:"●";color:var(--red);margin-right:4px}
.programs{position:absolute;left:28px;top:508px;display:flex;gap:8px}
.program{width:62px;height:62px;border-radius:50%;background:var(--white);border:3px solid var(--red);
  color:var(--red);font-weight:700;font-size:12.5px;line-height:15px;display:flex;align-items:center;
  justify-content:center;text-align:center}
.student-photo{position:absolute;left:525px;top:596px;width:326px;height:454px;
  background:linear-gradient(170deg,#e8d6c8 0%,#c98f86 55%,#b23a3d 100%);border-left:6px solid var(--red)}
.message{position:absolute;left:30px;top:650px;width:500px;padding:14px 14px;
  background:rgba(255,255,255,.88);font-weight:900;font-size:31px;line-height:46px;color:var(--navy);white-space:nowrap}
.message .accent{color:var(--red)}
.message p+p{margin-top:12px}
.footer{position:absolute;left:0;top:1093px;width:851px;height:107px;background:var(--white);
  border-top:4px solid var(--red)}
.brand{position:absolute;left:40px;top:20px;display:flex;align-items:center;gap:10px}
.brand-mark{width:26px;height:26px;border-radius:50%;background:var(--blue)}
.brand-name{font-family:"Montserrat",sans-serif;font-weight:700;font-size:28px;color:var(--navy)}
.url{position:absolute;left:78px;top:62px;font-size:15px;color:var(--navy);font-weight:500}
.see-back{position:absolute;left:730px;top:1120px;width:96px;height:56px;background:var(--red);
  color:var(--white);font-size:12px;font-weight:700;line-height:17px;display:flex;align-items:center;
  justify-content:center;text-align:center;white-space:nowrap}
</style>
</head>
<body>
<main class="flyer">
  <div class="backdrop" role="img" aria-label="パスポートと外貨紙幣の写真"></div>
  <div class="top-band">海外への教育旅行を準備中の生徒様・ご家族の方へ</div>

  <h1 class="headline">教育旅行先で<br><em>必要なお金の事前準備</em>を<br>お手伝いします!</h1>

  <div class="tags">
    <span class="tag">外貨両替サービス</span>
    <span class="tag">海外専用トラベルプリペイドカード</span>
  </div>

  <p class="intro">アフターコロナの現在、市中の銀行窓口のほとんどが外貨両替の取り扱いをしておらず、日本円から外貨の両替ができる場所は非常に限られています。空港の窓口においても、時間の制約があり両替に思わぬ時間を費やす事も多く、両替事情はよくありません。教育旅行では大切な時間を無駄にすることなく、スムーズに行動する事が重要です。当社では外貨両替に精通したスタッフが海外へご出発される生徒様の必要なお金を一括して準備するお手伝いをさせていただきます。</p>

  <div class="audience">小学生から大学・大学院生まで</div>
  <ul class="programs">
    <li class="program">サマー<br>スクール</li>
    <li class="program">ホーム<br>ステイ</li>
    <li class="program">語学研修</li>
    <li class="program">海外<br>修学旅行</li>
    <li class="program">留学</li>
    <li class="program">卒業旅行</li>
  </ul>

  <div class="student-photo" role="img" aria-label="スーツケースを持つ学生の写真"></div>

  <div class="message">
    <p>現地で使うお金の手配に関して<br>ご不安・ご心配をお持ちの方、<br><span class="accent">当社にご相談ください!</span></p>
    <p>当社の教育旅行品質の<br>外貨準備サービスを利用して<br><span class="accent">安心して海外へ!</span></p>
  </div>

  <footer class="footer">
    <div class="brand"><span class="brand-mark"></span><span class="brand-name">Tabisora Exchange</span></div>
    <div class="url">www.tabisora-exchange.jp</div>
  </footer>
  <div class="see-back">詳しくは裏面を<br>ご覧ください</div>
</main>
</body>
</html>
```